Business Card Design Project

Corvexa logo will be provided after
Front

Ned Marrowick- Construction Manager

Ph: (61) 07 53182079
nmarrowick@corvexa-example.com.au
PO Box 83 Kelvorin 4619

Back
Corvexa
EPCM

Oil - Gas - Mining

Industry/Entity Type

Business

Font styles to use
Sans Serif

Colors
faa54b

Requirements
Must have
• White Back Ground

```html
<!DOCTYPE html>
<html lang="en">
<head>
<meta charset="utf-8">
<title>Corvexa Business Card</title>
<link rel="stylesheet" href="https://fonts.googleapis.com/css2?family=Open+Sans:wght@400;600;700;800&display=swap">
<style>
  :root {
    --brand-orange: #f7921e;
    --ink: #1f1f1f;
    --card-white: #ffffff;
    --backdrop: #ecebe8;
  }
  * { box-sizing: border-box; margin: 0; padding: 0; }
  html, body {
    width: 1200px;
    height: 1000px;
    overflow: hidden;
    background: var(--backdrop);
    font-family: "Open Sans", Arial, sans-serif;
  }
  .canvas { position: relative; width: 1200px; height: 1000px; }
  .card {
    position: absolute;
    left: 265px;
    width: 665px;
    height: 396px;
    border-radius: 22px;
    overflow: hidden;
    box-shadow: 0 3px 10px rgba(0,0,0,0.18);
  }
  .card-front { top: 73px; background: var(--brand-orange); }
  .card-back { top: 533px; background: var(--card-white); }

  .front-wordmark {
    position: absolute;
    top: 166px;
    left: 0;
    width: 100%;
    text-align: center;
    color: var(--card-white);
    font-weight: 800;
    font-size: 60px;
    letter-spacing: 2px;
    line-height: 1;
  }
  .front-tagline {
    position: absolute;
    top: 256px;
    left: 0;
    width: 100%;
    text-align: center;
    color: var(--card-white);
    font-weight: 600;
    font-size: 15px;
    letter-spacing: 0.3px;
  }

  .back-wordmark {
    position: absolute;
    top: 62px;
    right: 25px;
    color: var(--ink);
    font-weight: 800;
    font-size: 46px;
    letter-spacing: 1px;
    line-height: 1;
  }
  .name-marker {
    position: absolute;
    left: 0;
    top: 175px;
    width: 12px;
    height: 41px;
    background: var(--brand-orange);
  }
  .person-name {
    position: absolute;
    left: 22px;
    top: 172px;
    color: var(--ink);
    font-weight: 700;
    font-size: 22px;
    line-height: 1.1;
  }
  .person-title {
    position: absolute;
    left: 22px;
    top: 199px;
    color: var(--brand-orange);
    font-size: 16px;
    line-height: 1.1;
  }
  .contact-list { position: absolute; left: 22px; top: 282px; list-style: none; }
  .contact-item {
    display: flex;
    align-items: center;
    gap: 8px;
    color: var(--ink);
    font-size: 16px;
    height: 23px;
  }
  .contact-item.address { margin-top: 10px; }
  .contact-icon { width: 14px; height: 14px; fill: var(--ink); flex: none; }
  .bottom-band {
    position: absolute;
    left: 0;
    bottom: 0;
    width: 100%;
    height: 11px;
    background: var(--brand-orange);
  }
</style>
</head>
<body>
<main class="canvas">
  <section class="card card-front" aria-label="Card front">
    <div class="front-wordmark">CORVEXA</div>
    <div class="front-tagline">OIL - GAS - MINING</div>
  </section>

  <section class="card card-back" aria-label="Card back">
    <div class="back-wordmark">CORVEXA</div>
    <div class="name-marker"></div>
    <div class="person-name">Ned Marrowick</div>
    <div class="person-title">Construction Manager</div>
    <ul class="contact-list">
      <li class="contact-item">
        <svg class="contact-icon" viewBox="0 0 24 24" aria-hidden="true"><path d="M6.6 10.8a15.1 15.1 0 0 0 6.6 6.6l2.2-2.2c.3-.3.7-.4 1-.2 1.1.4 2.3.6 3.6.6.6 0 1 .4 1 1V20c0 .6-.4 1-1 1A17 17 0 0 1 3 4c0-.6.4-1 1-1h3.5c.6 0 1 .4 1 1 0 1.3.2 2.5.6 3.6.1.3 0 .7-.2 1z"/></svg>
        <span>(61) 07 53182079</span>
      </li>
      <li class="contact-item">
        <svg class="contact-icon" viewBox="0 0 24 24" aria-hidden="true"><path d="M2 5h20v14H2z M3 6l9 7 9-7" fill="none" stroke="#1f1f1f" stroke-width="0"/><path d="M2 5h20v2l-10 7L2 7z"/><path d="M2 9l10 7 10-7v10H2z"/></svg>
        <span>nmarrowick@corvexa-example.com.au</span>
      </li>
      <li class="contact-item address">
        <svg class="contact-icon" viewBox="0 0 24 24" aria-hidden="true"><path d="M12 2a7 7 0 0 0-7 7c0 5.2 7 13 7 13s7-7.8 7-13a7 7 0 0 0-7-7zm0 9.5A2.5 2.5 0 1 1 12 6.5a2.5 2.5 0 0 1 0 5z"/></svg>
        <span>PO Box 83 Kelvorin 4619</span>
      </li>
    </ul>
    <div class="bottom-band"></div>
  </section>
</main>
</body>
</html>
```